High end personal training flyer design

I want a flyer designed to be delivered to people's houses to interest them in high end (and, therefore, not cheap) personal training services.

Don't want standard pictures of people exercising, before and afters, etc. More something that will appeal to that more affluent market.

Flexible on size of flyer, but please make sure it is a standard size that I can get printed easily. Would like it not to look like a normal flyer you get through the letterbox, so if any particular sizes, shapes, etc are known to do that, then that would be a good start.

Text on flyer to be as follows:

Is this you:

Live in East Cheshire
Male, aged 30-50
A father
Cash rich, time poor
Find handling high pressure at work comfortable
But have a short fuse out of work – with the wife, kids, life in general, etc
Not happy with the way your body looks and feels
Know exactly what you should do to sort that, but struggling to actually do it for various reasons
Turned off by the standard menu of options for addressing that – gyms, slimming clubs, diets, etc

If so, you may be interested in what I do.

Some would call it Personal Training. Some would call it Coaching. I’m not interested in giving what I do labels.

What I am interested in is providing the best possible service (and results) for my clients – whatever that entails.

I work closely with one or two clients at a time to make sure they get exactly what they need.

If you would like to find out more about this, I usually meet for a coffee and a chat. To see if we both think our working together is a good idea.

No squeeze pages, no countdowns, mailing lists or false scarcity.

No plastering this flyer with ‘Before and afters’ – they are ten a penny and my clients don’t want to have pictures of them in their underwear spread around the local area.

Just give me a call and we’ll go from there.

My number is 07912645320.

Tim

Industry/Entity Type

Training

Requirements
Should not have
• Generic before and after or exercise type pictures

```html
<!DOCTYPE html>
<html lang="en">
<head>
<meta charset="utf-8">
<title>Tim – Personal Training Flyer</title>
<link rel="stylesheet" href="https://fonts.googleapis.com/css2?family=Open+Sans:ital,wght@0,400;0,600;0,700;1,400;1,600;1,700&family=Roboto:wght@400;700;900&display=swap">
<style>
  :root {
    --coral: #f26b5f;
    --navy: #2e3a59;
    --ink: #3a3a3c;
    --band: #5d5c5e;
    --footer: #a5a5a7;
    --footer-deep: #6f6e70;
    --paper-top: #ffffff;
    --paper-bottom: #e6e6e8;
    --bubble: rgba(40, 40, 42, 0.82);
    --white: #ffffff;
    --stage: #ffffff;
  }
  * { margin: 0; padding: 0; box-sizing: border-box; }
  html, body { width: 1200px; height: 848px; overflow: hidden; background: var(--stage); }
  .canvas { position: relative; width: 1200px; height: 848px; }
  .page {
    position: absolute; top: 26px; width: 562px; height: 800px; overflow: hidden;
    background: linear-gradient(160deg, var(--paper-top) 0%, #f3f3f4 45%, var(--paper-bottom) 100%);
    box-shadow: 0 2px 8px rgba(0,0,0,0.25);
    font-family: "Open Sans", Arial, sans-serif;
  }
  .page--front { left: 30px; }
  .page--back { left: 612px; }
  .page__art { position: absolute; inset: 0; width: 562px; height: 800px; }

  .headline {
    position: absolute; left: 96px; top: 74px;
    font-family: "Roboto", Arial, sans-serif; font-weight: 900; font-size: 52px;
    letter-spacing: -1px; color: var(--navy); line-height: 1;
  }
  .headline__accent { color: var(--coral); }

  .trait {
    position: absolute; border-radius: 50%;
    background: var(--bubble); border: 2px solid rgba(20,20,20,0.6);
    color: var(--white); display: flex; align-items: center; justify-content: center;
    text-align: center; font-size: 18px; line-height: 1.1; padding: 8px;
  }
  .trait__text { display: block; }
  .trait__small { display: block; font-size: 12px; margin-top: 4px; }
  .trait--sm { width: 104px; height: 104px; }
  .trait--lg { width: 168px; height: 168px; font-size: 23px; line-height: 1.1; padding: 14px; }
  .trait--note { font-size: 15px; }
  .trait--tiny { font-size: 12px; }

  .figure {
    position: absolute;
    background: linear-gradient(180deg, #6b4a3a 0%, #e9b99a 22%, var(--coral) 40%, var(--coral) 58%, var(--navy) 62%, var(--navy) 94%, #6b4a3a 100%);
    border-radius: 40px 40px 6px 6px; opacity: 0.9;
  }
  .figure--front { left: 166px; top: 150px; width: 168px; height: 456px; }
  .figure--tall { left: 312px; top: 48px; width: 102px; height: 368px; }
  .figure--short { left: 422px; top: 66px; width: 106px; height: 308px; }

  .tagline {
    position: absolute; left: 0; right: 0; top: 624px; text-align: center;
    font-style: italic; font-weight: 600; font-size: 24px; line-height: 1.2; color: var(--white);
  }

  .footer { position: absolute; left: 0; right: 0; top: 682px; height: 100px; background: var(--footer); }
  .footer__strip { position: absolute; left: 0; right: 0; top: 782px; height: 18px; background: var(--footer-deep); }
  .footer__name {
    position: absolute; left: 72px; top: 706px;
    font-family: "Roboto", Arial, sans-serif; font-weight: 900; font-size: 50px; color: var(--white); line-height: 1;
  }
  .footer__badge {
    position: absolute; left: 210px; top: 703px; width: 56px; height: 56px;
    border-radius: 50%; background: var(--coral);
  }
  .footer__phone {
    position: absolute; left: 278px; top: 715px;
    font-family: "Roboto", Arial, sans-serif; font-weight: 700; font-size: 33px; color: var(--white); line-height: 1;
  }

  .intro {
    position: absolute; left: 70px; top: 60px; width: 200px;
    font-style: italic; font-weight: 700; font-size: 19px; line-height: 1.35; color: var(--navy);
  }
  .mission {
    position: absolute; left: 80px; top: 186px; width: 232px;
    font-style: italic; font-weight: 600; font-size: 21px; line-height: 1.35; color: #5a5a5c;
  }
  .promise {
    position: absolute; left: 0; right: 0; top: 440px; text-align: center;
    font-family: "Roboto", Arial, sans-serif; font-weight: 900; font-size: 23px; line-height: 1.3; color: var(--ink);
  }
  .approach {
    position: absolute; left: 0; right: 0; top: 546px; text-align: center;
    font-size: 15px; line-height: 1.4; color: var(--white);
  }
  .invite {
    position: absolute; left: 0; right: 0; top: 604px; text-align: center;
    font-size: 15px; line-height: 1.35; color: var(--white);
  }
  .invite__lead { font-size: 21px; font-weight: 600; line-height: 1.4; }
</style>
</head>
<body>
<main class="canvas">

  <section class="page page--front">
    <svg class="page__art" viewBox="0 0 562 800" aria-hidden="true">
      <polygon points="0,540 562,508 562,682 0,682" fill="#5d5c5e"/>
      <polyline points="0,540 562,508" fill="none" stroke="#f26b5f" stroke-width="6"/>
      <polyline points="130,42 58,42 58,600 150,600 150,550" fill="none" stroke="#f26b5f" stroke-width="14"/>
      <polyline points="398,36 428,36 428,530" fill="none" stroke="#f26b5f" stroke-width="14"/>
    </svg>

    <h1 class="headline">IS THIS <span class="headline__accent">YOU?</span></h1>

    <div class="trait trait--sm" style="left:34px; top:132px;"><span class="trait__text">Male,<span class="trait__small">aged 30-50</span></span></div>
    <div class="trait trait--sm" style="left:34px; top:249px;"><span class="trait__text">Live in<br>East<br>Cheshire</span></div>
    <div class="trait trait--sm" style="left:34px; top:366px;"><span class="trait__text">A<br>father</span></div>
    <div class="trait trait--sm trait--note" style="left:34px; top:471px;"><span class="trait__text">Cash<br>rich time<br>poor</span></div>

    <div class="trait trait--sm trait--note" style="left:386px; top:135px;"><span class="trait__text">short fuse<br>out of<br>work</span></div>
    <div class="trait trait--lg" style="left:354px; top:220px;"><span class="trait__text">Not HAPPY<br>with YOUR<br>BODY</span></div>
    <div class="trait trait--sm trait--tiny" style="left:386px; top:362px;"><span class="trait__text">Turned off<br>by the<br>standard<br>options</span></div>
    <div class="trait trait--sm trait--note" style="left:386px; top:468px;"><span class="trait__text">handling<br>high<br>pressure</span></div>

    <div class="figure figure--front" role="img" aria-label="Flat illustration of a bearded man in glasses, coral t-shirt and navy trousers"></div>

    <p class="tagline">If so, you may be interested in what I do.</p>

    <div class="footer"></div>
    <div class="footer__strip"></div>
    <div class="footer__name">TIM</div>
    <div class="footer__badge" role="img" aria-label="Call now badge"></div>
    <div class="footer__phone">07912645320</div>
  </section>

  <section class="page page--back">
    <svg class="page__art" viewBox="0 0 562 800" aria-hidden="true">
      <polygon points="0,524 562,508 562,682 0,682" fill="#5d5c5e"/>
      <polyline points="0,524 562,508" fill="none" stroke="#f26b5f" stroke-width="6"/>
      <polyline points="372,100 372,34 42,34 42,432 84,386 300,386" fill="none" stroke="#f26b5f" stroke-width="14"/>
      <path d="M500 330 C 540 370, 520 420, 460 420 L 430 414" fill="none" stroke="#2b2b2b" stroke-width="2.5"/>
      <polyline points="444,404 430,414 444,424" fill="none" stroke="#2b2b2b" stroke-width="2.5"/>
    </svg>

    <p class="intro">Personal Training. Coaching. I’m not interested in giving what I do labels.</p>
    <p class="mission">What I am interested in is providing the best possible service (and results) for my clients – whatever that entails.</p>

    <div class="figure figure--tall" role="img" aria-label="Flat illustration of the trainer in glasses, coral t-shirt and navy trousers"></div>
    <div class="figure figure--short" role="img" aria-label="Smaller flat illustration of the same trainer"></div>

    <p class="promise">NO SQUEEZE PAGES, NO COUNTDOWNS,<br>MAILING LISTS OR FALSE SCARCITY.</p>

    <p class="approach">I work closely with one or two clients at a time<br>to make sure they get exactly what they need.</p>
    <p class="invite"><span class="invite__lead">If you would like to find out more about this,</span><br>I usually meet for a coffee and a chat.<br>To see if we both think our working together is a good idea.</p>

    <div class="footer"></div>
    <div class="footer__strip"></div>
    <div class="footer__name">TIM</div>
    <div class="footer__badge" role="img" aria-label="Call now badge"></div>
    <div class="footer__phone">07912645320</div>
  </section>

</main>
</body>
</html>
```